BrambleWorks business card

Looking for business card design that supports our company/software values. We have 2 logo designs at the moment but open to change if you think you can enhance the brand. Check out website www.brambleworks.com.au.

Target Market(s)

Education

Contact Information for Business Card

Name, title, mobile, email and website

Font styles to use
Sans Serif

Colors

Designer to choose colors to be used in the design.

Requirements
Must have
• BrambleWorks logo with tree and tagline on rear side with dark grey background colour

```html
<!DOCTYPE html>
<html lang="en">
<head>
<meta charset="utf-8">
<title>BrambleWorks business card</title>
<link href="https://fonts.googleapis.com/css2?family=Arimo:wght@400&display=swap" rel="stylesheet">
<style>
  :root {
    --page: #e7e7e7;
    --card-dark: #1f2227;
    --card-mid: #2a2e33;
    --accent: #f2a91b;
    --text-light: #f2f2f2;
    --brand-grey: #5b6067;
    --muted: #4f545a;
    --rule: #4b4f54;
  }
  * { margin: 0; padding: 0; box-sizing: border-box; }
  html, body {
    width: 1200px; height: 1000px; overflow: hidden;
    background: var(--page);
    font-family: "Arimo", Arial, sans-serif;
  }
  .card {
    position: absolute; left: 190px;
    width: 1000px; height: 571px;
    transform: scale(0.82); transform-origin: top left;
    background: linear-gradient(115deg, var(--card-dark) 0%, var(--card-mid) 100%);
    box-shadow: 0 4px 14px rgba(0,0,0,0.18);
  }
  .card-back { top: 22px; }
  .card-front { top: 510px; }

  /* rear side */
  .back-mark {
    position: absolute; left: 130px; top: 180px;
    width: 120px; height: 120px; border-radius: 50%;
    background: var(--brand-grey);
  }
  .back-name {
    position: absolute; left: 300px; top: 170px;
    font-size: 88px; color: var(--brand-grey); line-height: 1;
  }
  .back-rule {
    position: absolute; left: 300px; top: 282px;
    width: 600px; height: 2px; background: var(--rule);
  }
  .back-tagline {
    position: absolute; left: 300px; top: 298px;
    font-size: 40px; color: var(--accent); letter-spacing: 0.5px;
  }
  .back-web {
    position: absolute; left: 130px; top: 440px;
    font-size: 24px; color: var(--muted);
  }

  /* front side */
  .brand {
    position: absolute; left: 92px; top: 250px;
    display: flex; align-items: center; gap: 16px;
  }
  .brand-dot {
    width: 34px; height: 34px; border-radius: 50%;
    background: var(--brand-grey);
  }
  .brand-name { font-size: 42px; color: var(--brand-grey); letter-spacing: 0.5px; }
  .person { position: absolute; right: 40px; top: 328px; text-align: right; }
  .person-name { font-size: 37px; color: var(--accent); line-height: 1.1; }
  .person-title { font-size: 27px; color: var(--text-light); line-height: 1.3; }
  .rule {
    position: absolute; left: 48px; right: 42px; top: 410px;
    height: 4px; background: var(--rule);
  }
  .address {
    position: absolute; left: 51px; top: 430px;
    color: var(--text-light); font-size: 22px; line-height: 35px;
  }
  .address-pin { display: block; margin: 0 0 6px 70px; }
  .contacts {
    position: absolute; right: 42px; top: 432px;
    list-style: none; color: var(--text-light); font-size: 18px;
  }
  .contacts li {
    display: flex; justify-content: flex-end; align-items: center;
    gap: 20px; height: 34px;
  }
  .contacts svg { width: 24px; height: 24px; }
</style>
</head>
<body>
  <section class="card card-back" aria-label="BrambleWorks business card, rear side">
    <span class="back-mark"></span>
    <p class="back-name">BrambleWorks</p>
    <div class="back-rule"></div>
    <p class="back-tagline">Student Success Platform</p>
    <p class="back-web">www.brambleworks.com.au</p>
  </section>

  <section class="card card-front" aria-label="BrambleWorks business card, front side">
    <div class="brand">
      <span class="brand-dot"></span>
      <span class="brand-name">BrambleWorks</span>
    </div>

    <div class="person">
      <p class="person-name">ALEX MORGAN</p>
      <p class="person-title">Manager</p>
    </div>

    <div class="rule"></div>

    <div class="address">
      <svg class="address-pin" width="24" height="30" viewBox="0 0 24 30" aria-hidden="true">
        <path d="M12 0C5.4 0 0 5.3 0 11.8 0 20 12 30 12 30s12-10 12-18.2C24 5.3 18.6 0 12 0z" fill="var(--accent)"/>
        <circle cx="12" cy="11.5" r="4.5" fill="var(--card-dark)"/>
      </svg>
      <p>42 Fernhill Road</p>
      <p>Hobart, Tasmania 7000</p>
    </div>

    <ul class="contacts">
      <li>04123456789
        <svg viewBox="0 0 24 24" aria-hidden="true"><path d="M6.6 2.5l3 3.6-1.8 2.4c1.2 2.8 3.4 5 6.2 6.4l2.4-1.8 3.6 3-1.6 3.4C10.5 19.6 4.2 13.3 3.2 4.1z" fill="var(--accent)"/></svg>
      </li>
      <li>alex@brambleworks.com.au
        <svg viewBox="0 0 24 24" aria-hidden="true"><rect x="1" y="5" width="22" height="15" fill="var(--accent)"/><path d="M1 5l11 8 11-8" fill="none" stroke="var(--card-dark)" stroke-width="1.6"/></svg>
      </li>
      <li>www.brambleworks.com.au
        <svg viewBox="0 0 24 24" aria-hidden="true"><g fill="none" stroke="var(--accent)" stroke-width="1.8"><circle cx="12" cy="12" r="10"/><ellipse cx="12" cy="12" rx="4.5" ry="10"/><path d="M2 12h20M4 6.5h16M4 17.5h16"/></g></svg>
      </li>
    </ul>
  </section>
</body>
</html>
```